Medical supplies company needs a catalogue re-design

Our present catalogue is spread over a number of pages but this needs to be reduced. 4-5 images would require to be on each page. It needs to be professional, simple and elegant. The photos and descriptors need to be adjacent to each other. It should be able to be emailed conventionally as an e-catalogue without it being compressed. an email with existing catalogue will be emailed to anyone interested.
https://www.quillvault.net/s/81tazup7rqwmdlon/consumables%20photos%20and%20descriptions.pdf?dl=0
Target Market(s)
medical practices, hospitals
Industry/Entity Type
Medical Supply

```html
<!DOCTYPE html>
<html lang="en">
<head>
<meta charset="utf-8">
<title>Wound Care – Catalogue Page</title>
<link href="https://fonts.googleapis.com/css2?family=Gelasio:ital,wght@0,400;0,700;1,400&display=swap" rel="stylesheet">
<style>
  :root {
    --page-bg: #b5e6f6;
    --sheet: #ffffff;
    --accent: #0fb0e8;
    --ink: #1c1c1c;
    --frame: #555555;
    --tone-blue-a: #4a7bbf;
    --tone-blue-b: #2f559b;
    --tone-pink-a: #e6cfc7;
    --tone-pink-b: #d7b8ad;
    --tone-cream-a: #efeadf;
    --tone-cream-b: #ddd5c3;
    --tone-grey-a: #f6f6f6;
    --tone-grey-b: #dedede;
  }
  * { margin: 0; padding: 0; box-sizing: border-box; }
  html, body { width: 1200px; height: 848px; overflow: hidden; }
  body {
    background: var(--page-bg);
    font-family: "Gelasio", Georgia, serif;
    color: var(--ink);
    position: relative;
  }
  .page-title {
    position: absolute; left: 0; top: 0; width: 1200px; height: 39px;
    text-align: center; font-size: 38px; font-weight: 700; line-height: 38px;
    color: var(--accent);
  }
  .sheet {
    position: absolute; left: 39px; top: 39px; width: 1122px; height: 770px;
    background: var(--sheet);
  }
  .rule { position: absolute; background: var(--accent); }
  .photo { position: absolute; border: 1px solid var(--frame); }
  .photo--tape, .photo--strips { background: linear-gradient(180deg, var(--tone-blue-a), var(--tone-blue-b)); }
  .photo--elastic { background: linear-gradient(180deg, var(--tone-pink-a), var(--tone-pink-b)); }
  .photo--crepe { background: linear-gradient(180deg, var(--tone-cream-a), var(--tone-cream-b)); }
  .photo--film { background: linear-gradient(180deg, var(--tone-grey-a), var(--tone-grey-b)); }
  .product { position: absolute; }
  .product h2 {
    font-size: 18.6px; font-weight: 700; line-height: 22.4px; margin-bottom: 9px;
  }
  .features { list-style: none; font-size: 14.2px; line-height: 17.2px; }
  .features li { position: relative; padding-left: 24px; }
  .features li::before {
    content: ""; position: absolute; left: 4px; top: 4px;
    width: 8px; height: 8px; background: var(--accent);
    transform: rotate(45deg) scaleY(1.25);
  }
  .pack { font-size: 14.2px; font-style: italic; line-height: 18px; }
  .lead { font-size: 15.6px; font-style: italic; line-height: 19px; }
  .spec { font-size: 14.2px; line-height: 17.2px; }
  .spec b { font-weight: 700; }
</style>
</head>
<body>
  <h1 class="page-title">Wound Care</h1>
  <div class="sheet"></div>

  <div class="rule" style="left:58px;top:278px;width:528px;height:3px"></div>
  <div class="rule" style="left:598px;top:54px;width:3px;height:445px"></div>
  <div class="rule" style="left:609px;top:238px;width:528px;height:3px"></div>
  <div class="rule" style="left:58px;top:507px;width:1094px;height:3px"></div>

  <div class="photo photo--tape" role="img" aria-label="Photo: roll of white nonwoven tape"
       style="left:60px;top:57px;width:242px;height:212px"></div>
  <div class="product" style="left:324px;top:60px;width:252px">
    <h2>High Quality Nonwoven Tape</h2>
    <ul class="features">
      <li>Non-allergenic and suitable for the most sensitive and soft skin.</li>
      <li>Box of 10</li>
    </ul>
  </div>

  <div class="photo photo--strips" role="img" aria-label="Photo: box and pack of wound closure strips"
       style="left:58px;top:300px;width:243px;height:178px"></div>
  <div class="product" style="left:324px;top:298px;width:252px">
    <h2>Wound Closure Strips</h2>
    <ul class="features">
      <li>Reinforced strips of microporous material for fast and effective wound closure or to be applied to wounds that have been stitched to provide extra tensile support.</li>
      <li>3mm by 75mm (five pcs per pack-age, 50 packages in a box)</li>
      <li>6mm by 75mm (three pcs per pack-age, 50 packages in a box)</li>
    </ul>
  </div>

  <div class="photo photo--elastic" role="img" aria-label="Photo: wrapped rolls of skin colour elastic bandage"
       style="left:612px;top:57px;width:186px;height:176px"></div>
  <div class="product" style="left:806px;top:60px;width:335px">
    <h2>Skin Colour High Elastic Bandages (7.5 cm x 4.5 m, 10cm x 4.5 m)</h2>
    <ul class="features">
      <li>ideal for treatment, after-care &amp; prevention of sports injuries</li>
      <li>secured with lightweight metal clips</li>
      <li>knit design offers strength, comfort &amp; breathability</li>
      <li>individually wrapped</li>
    </ul>
    <p class="pack">(12 rolls per box)</p>
  </div>

  <div class="photo photo--crepe" role="img" aria-label="Photo: wrapped rolls of unbleached crepe bandage"
       style="left:612px;top:248px;width:186px;height:251px"></div>
  <div class="product" style="left:806px;top:248px;width:335px">
    <h2>Unbleached Crepe<br>Elastic Bandages<br>(7.5 cm x 4.5 m, 10cm x 4.5 m)</h2>
    <ul class="features">
      <li>Ideal for holding dressings in place</li>
      <li>can be used for strapping</li>
    </ul>
    <p class="pack">(12 rolls per box)</p>
  </div>

  <div class="photo photo--film" role="img" aria-label="Photo: packaged film dressing and an unwrapped dressing with pad"
       style="left:60px;top:526px;width:238px;height:277px"></div>
  <div class="product" style="left:324px;top:526px;width:800px">
    <h2 style="margin-bottom:5px">Film Island Dressing Without Pad</h2>
    <p class="lead">These dressings are waterproof, and sterile. They allow the wound to breathe and are used for minor wounds. Can also be used with sterile gauze for minor wounds and burns.</p>
    <p class="spec">1. Made of transparent PU film<br>2. Keeps wound dry and protects against water, dirt and bacteria 3. 50 per box<br><b>Sizes:</b> 4.4cm by 4.4cm and 6cm by 7cm</p>
  </div>
  <div class="product" style="left:324px;top:675px;width:800px">
    <h2 style="margin-bottom:5px">Film Island Dressing with Pad</h2>
    <p class="lead">Waterproof dressings with a pad to absorb wound exudate. These are used following surgical procedures to cover wounds to prevent infection.</p>
    <p class="spec">1. Made of transparent PU film with gauze pad in the centre<br>2. Acts as a barrier to bacteria, debris and water 3. 50 pcs per box<br><b>Sizes:</b> 6cm by 7cm, 7cm by 10cm, 10cm by 12cm, 10cm by 15cm, 10cm by 20cm</p>
  </div>
</body>
</html>
```